Cloud Hosting Provider Web Site

We need to create the design for Nimbo-Pails.net a new Cloud Hosting Provider Website.

We already have a logo and a draft website with preliminary content showing the desired structure for the final web site.

I need a design for the Home Page and all 10 Internal web pages currently linked from the draft home page.

The documentation site (/docs) Customer Portal (/portal) and Support site (/support) are not part of this design project.

We need images to illustrate all pages which of course need to be consistent with the content. Please read carefully the text of each page in the draft web site to understand the purpose of each page and illustrate it accordingly.

All pages must be illustrated with images, I do not want any single page with just text.

I want to maintain the slides idea of the draft website home page.

The web site must look professional, we are competitors of huge companies like tallow grid systems (tgs.tallowgrid.com), Velquist Oriel (oriel.velquist.com) and DuneLoft (www.duneloft.com) so we need to look as serious as them.

You may download the draft web site pages to style them, I need fully finalized HTML / CSS and image files.

A top link bar and link footer must be included in every page.

Also the web site will have the possibility to start a chat conversation with a sales agent, so a graphical link to do so must be included in the design, together with a chat window design (including HTML/CSS)

Information for accessing the draft web site follows:

URL: www.nimbo-pails.net
username: design
password: QOPqop987654

If you need any additional information please let me know.

```html
<!DOCTYPE html>
<html lang="en">
<head>
<meta charset="utf-8">
<title>Nimbo-Pails.net — Private Cloud Hosting</title>
<link href="https://fonts.googleapis.com/css2?family=Fira+Sans:wght@400;500;600;700&family=Exo+2:ital,wght@1,500;1,600&family=Roboto:ital,wght@0,400;0,500;1,400&display=swap" rel="stylesheet">
<style>
:root{
  --navy:#1b2333;
  --blue:#1aa3e0;
  --deep:#1d3c5e;
  --footer:#1c4672;
  --ink:#2b2b2b;
  --card:#efefef;
  --line:#d4d4d4;
  --white:#ffffff;
}
*{margin:0;padding:0;box-sizing:border-box}
html,body{width:947px;height:1200px;overflow:hidden;background:var(--white)}
body{position:relative;font-family:"Fira Sans",sans-serif;color:var(--ink)}
.abs{position:absolute}

/* top bar */
.topbar{left:0;top:0;width:947px;height:22px;background:var(--navy);color:var(--white)}
.tagline{left:187px;top:4px;font:italic 400 12px "Roboto",sans-serif}
.topbar-divider{left:500px;top:0;width:1px;height:22px;background:#34405a}
.live-help{left:582px;top:5px;font:500 10px "Roboto",sans-serif;display:flex;align-items:center;gap:6px}
.chat-btn{left:782px;top:0;width:85px;height:22px;background:var(--blue);font:600 10.5px "Fira Sans",sans-serif;color:var(--white);display:flex;align-items:center;justify-content:center}

/* nav */
.navbar{left:0;top:22px;width:947px;height:52px;background:linear-gradient(#ffffff,#f3f3f3);border-bottom:1px solid #e2e2e2}
.brand{left:104px;top:30px;display:flex;align-items:center;gap:6px;font:600 14px "Fira Sans",sans-serif;color:var(--deep)}
.brand-dot{width:16px;height:16px;border-radius:50%;background:var(--blue)}
.nav{left:291px;top:43px;display:flex;font:600 12px "Fira Sans",sans-serif;color:var(--deep)}
.nav a{color:inherit;text-decoration:none;position:absolute;white-space:nowrap}
.nav a.active{color:var(--blue)}
.nav-underline{left:291px;top:71px;width:34px;height:3px;background:var(--blue)}

/* hero */
.hero{left:0;top:74px;width:947px;height:332px;background:linear-gradient(100deg,#6d6c6a 0%,#9a9894 22%,#c9d3dc 42%,#a9b9c8 62%,#6f8294 82%,#8ea0b2 100%)}
.hero-text{left:520px;top:146px;width:300px;text-align:center;font:italic 600 21px/25px "Exo 2",sans-serif;color:var(--blue)}

/* features */
.features{left:0;top:406px;width:947px;height:78px;background:var(--white)}
.feature-ring{width:70px;height:70px;border-radius:50%;background:var(--white);border:3px solid #3a3f4a;border-bottom-color:transparent;border-left-color:#8a8f99;border-right-color:#8a8f99;display:flex;align-items:flex-start;justify-content:center;padding-top:17px}
.feature-label{width:150px;text-align:center;font:500 11.5px/15.5px "Fira Sans",sans-serif;color:var(--blue)}
.divider{left:0;top:483px;width:947px;border-top:1px dashed var(--line)}
.mark{left:462px;top:522px;width:26px;height:26px;border-radius:50%;background:var(--blue)}

/* cards */
.card{width:222px;background:var(--card);border-top:3px solid var(--blue)}
.card.first{border-top-color:var(--deep)}
.card-img{position:absolute;left:7px;top:8px;width:207px;height:85px}
.card-title{position:absolute;left:0;width:222px;text-align:center;font:500 11.5px/16.5px "Fira Sans",sans-serif;color:var(--ink)}
.card-title.accent{color:var(--blue)}

/* footer */
.footer{left:0;top:1101px;width:947px;height:65px;background:var(--footer);color:var(--white)}
.footer-text{font:400 13.5px/19px "Fira Sans",sans-serif}
.social{width:30px;height:30px;border-radius:50%;background:var(--white)}
.bottombar{left:0;top:1166px;width:947px;height:34px;background:linear-gradient(#2a2a2a,#000)}
.bottom-links{left:104px;top:1176px;font:400 10px "Fira Sans",sans-serif;color:#e6e6e6;display:flex;gap:5px}
.bottom-links span.sep{color:#aaa}
.copyright{right:79px;top:1176px;font:400 10px "Fira Sans",sans-serif;color:#e6e6e6}
</style>
</head>
<body>

<header>
  <div class="abs topbar"></div>
  <div class="abs tagline" style="color:#fff">Create Your Own Private Cloud, Pail By Pail</div>
  <div class="abs topbar-divider"></div>
  <div class="abs live-help" style="color:#fff">
    <svg width="13" height="13" viewBox="0 0 16 16" fill="none" stroke="#fff" stroke-width="1.6"><path d="M3 9V7a5 5 0 0 1 10 0v2"/><rect x="2" y="8" width="3" height="5" rx="1"/><rect x="11" y="8" width="3" height="5" rx="1"/></svg>
    LIVE HELP ONLINE : 17-800-45120
  </div>
  <a class="abs chat-btn">Chat With Us!</a>

  <div class="abs navbar"></div>
  <div class="abs brand"><span class="brand-dot"></span>Nimbo-Pails.net</div>
  <nav class="abs nav">
    <a class="active" style="left:0">Home</a>
    <a style="left:55px">Use Cases</a>
    <a style="left:134px">Cloud Services</a>
    <a style="left:239px">Pail's Infrastructure</a>
    <a style="left:384px">Our Company</a>
    <a style="left:485px">Customer Login</a>
  </nav>
  <div class="abs nav-underline"></div>
</header>

<section>
  <div class="abs hero" role="img" aria-label="Photo of a business person holding a tablet with a cloud floating above it, in front of server racks and wall monitors"></div>
  <div class="abs hero-text">Each PAIL<br>Just $ 990 Per Month!</div>
</section>

<section class="features-row">
  <div class="abs features"></div>

  <div class="abs feature-ring" style="left:139px;top:372px">
    <svg width="24" height="24" viewBox="0 0 24 24" fill="#1d3c5e"><rect x="2" y="3" width="20" height="8" rx="1"/><rect x="2" y="13" width="20" height="8" rx="1"/><rect x="5" y="16" width="6" height="2" fill="#fff"/><rect x="5" y="6" width="6" height="2" fill="#fff"/></svg>
  </div>
  <div class="abs feature-label" style="left:99px;top:432px">Dedicated<br>Redundant Hardware</div>

  <div class="abs feature-ring" style="left:263px;top:372px">
    <svg width="24" height="24" viewBox="0 0 24 24" fill="none" stroke="#1d3c5e" stroke-width="1.6"><rect x="5" y="5" width="14" height="14"/><rect x="9" y="9" width="6" height="6" fill="#1d3c5e"/><path d="M8 2v3M12 2v3M16 2v3M8 19v3M12 19v3M16 19v3M2 8h3M2 12h3M2 16h3M19 8h3M19 12h3M19 16h3"/></svg>
  </div>
  <div class="abs feature-label" style="left:223px;top:432px">32 CPU<br>Cores</div>

  <div class="abs feature-ring" style="left:387px;top:372px">
    <svg width="24" height="24" viewBox="0 0 24 24" fill="#1d3c5e"><rect x="7" y="2" width="10" height="20" rx="1"/><path d="M4 5h3M4 9h3M4 13h3M4 17h3M17 5h3M17 9h3M17 13h3M17 17h3" stroke="#1d3c5e" stroke-width="1.6"/></svg>
  </div>
  <div class="abs feature-label" style="left:347px;top:432px">128 GB<br>RAM</div>

  <div class="abs feature-ring" style="left:511px;top:372px">
    <svg width="24" height="24" viewBox="0 0 24 24"><rect x="5" y="2" width="14" height="20" rx="2" fill="#1d3c5e"/><text x="12" y="14" text-anchor="middle" font-family="Fira Sans,sans-serif" font-size="5" font-weight="700" fill="#fff">SSD</text></svg>
  </div>
  <div class="abs feature-label" style="left:471px;top:432px">4 TB SSD Storage<br>/ Unlimited iops</div>

  <div class="abs feature-ring" style="left:634px;top:372px">
    <svg width="26" height="24" viewBox="0 0 26 24" fill="none" stroke="#1d3c5e" stroke-width="2.2"><path d="M4 19a10 10 0 1 1 18 0"/><path d="M13 15l5-6"/></svg>
  </div>
  <div class="abs feature-label" style="left:594px;top:432px">100 Mbps<br>Bandwidth</div>

  <div class="abs feature-ring" style="left:759px;top:372px">
    <svg width="30" height="24" viewBox="0 0 30 24" fill="none" stroke="#1d3c5e" stroke-width="1.8"><path d="M8 20h15a5 5 0 0 0 0-10 7 7 0 0 0-13-1 5.5 5.5 0 0 0-2 11z"/><circle cx="15" cy="14" r="2.5"/></svg>
  </div>
  <div class="abs feature-label" style="left:719px;top:432px">Free Cloud<br>Management Software</div>

  <div class="abs divider"></div>
  <div class="abs mark"></div>
</section>

<section class="use-cases">
  <article class="abs card first" style="left:104px;top:579px;height:147px">
    <div class="card-img" role="img" aria-label="Photo of hands releasing glowing cubes in a server room" style="background:linear-gradient(90deg,#b9c2cc,#eef1f4 35%,#8e8d8a 70%,#c5ccd4)"></div>
    <div class="card-title accent" style="top:104px">Start Your Own<br>Hosting Business</div>
  </article>
  <article class="abs card" style="left:363px;top:579px;height:147px">
    <div class="card-img" role="img" aria-label="Photo of a bright data center hall with rows of racks" style="background:linear-gradient(#e8ecf0,#b4bcc5 45%,#3a4049 60%,#cfd3d8)"></div>
    <div class="card-title" style="top:104px">Virtualize Your Current<br>Physical Infraestructure</div>
  </article>
  <article class="abs card" style="left:622px;top:579px;height:147px">
    <div class="card-img" role="img" aria-label="Illustration of a glowing cloud network on a purple background" style="background:linear-gradient(120deg,#3a2a7a,#8a7ad0 45%,#c8c4ef 55%,#3b3a95)"></div>
    <div class="card-title" style="top:104px">Moving From The Public<br>to The Private Cloud</div>
  </article>

  <article class="abs card" style="left:104px;top:748px;height:162px">
    <div class="card-img" role="img" aria-label="Photo of a business person holding a glowing cloud icon" style="background:linear-gradient(120deg,#0a3c5a,#1aa3e0 45%,#d9e6ee 60%,#0b2f49)"></div>
    <div class="card-title" style="top:104px">Saving Money With<br>The Private Cloud</div>
  </article>
  <article class="abs card" style="left:363px;top:748px;height:162px">
    <div class="card-img" role="img" aria-label="Photo of a corridor between server cabinets" style="background:linear-gradient(90deg,#7c7d7d,#b8b9b8 40%,#e6e3d2 70%,#8d8e8d)"></div>
    <div class="card-title" style="top:104px">Nimbo-Pails<br>Technical Features</div>
  </article>
  <article class="abs card" style="left:622px;top:748px;height:162px">
    <div class="card-img" role="img" aria-label="Illustration of connected pipes and office icons representing a management platform" style="background:linear-gradient(90deg,#f4f6f8,#e4ecf1 50%,#f7efd8)"></div>
    <div class="card-title" style="top:104px">Documentation :<br>Introducing Nimbo-Pails Virtual<br>Datacenter Management Platform</div>
  </article>

  <article class="abs card" style="left:104px;top:934px;height:133px">
    <div class="card-img" role="img" aria-label="Illustration of a glowing cloud linked to devices on a dark blue background" style="background:radial-gradient(circle at 45% 45%,#3d56d6,#0e1a55 45%,#05081c)"></div>
    <div class="card-title" style="top:103px">Cloud Services</div>
  </article>
  <article class="abs card" style="left:363px;top:934px;height:133px">
    <div class="card-img" role="img" aria-label="Photo of a support team wearing headsets" style="background:linear-gradient(90deg,#8a6b55,#e8e6e3 40%,#c9b6a3 70%,#eef0f2)"></div>
    <div class="card-title" style="top:103px">7x24x365 Support</div>
  </article>
  <article class="abs card" style="left:622px;top:934px;height:133px">
    <div class="card-img" role="img" aria-label="Photo of stacked coins" style="background:linear-gradient(90deg,#e6e8ea,#c8c4b8 40%,#b8875a 65%,#e4e6e8)"></div>
    <div class="card-title" style="top:103px">Pricing</div>
  </article>
</section>

<footer>
  <div class="abs footer"></div>
  <div class="abs footer-text" style="left:105px;top:1115px;color:#fff">We've got your back<br>24x7x365</div>
  <svg class="abs" style="left:316px;top:1117px" width="34" height="34" viewBox="0 0 24 24" fill="#fff"><path d="M6.6 2.5l2.8 3.6-1.8 2.3c1.3 2.8 3.2 4.8 6 6l2.3-1.8 3.6 2.8-1.6 3.4C11 18.5 5.5 13 3.2 4.1z"/></svg>
  <div class="abs footer-text" style="left:363px;top:1115px;color:#fff">LIVE HELP ONLINE :<br>17-800-45120</div>
  <svg class="abs" style="left:566px;top:1120px" width="42" height="30" viewBox="0 0 42 30" fill="none" stroke="#fff" stroke-width="1.8"><rect x="1" y="1" width="40" height="28" rx="3"/><path d="M1 2l20 15L41 2M1 28l14-12M41 28L27 16"/></svg>
  <div class="abs footer-text" style="left:624px;top:1125px;color:#fff">Email Us</div>
  <div class="abs social" style="left:758px;top:1119px"></div>
  <div class="abs social" style="left:797px;top:1119px"></div>
  <div class="abs social" style="left:837px;top:1119px"></div>

  <div class="abs bottombar"></div>
  <div class="abs bottom-links">
    <span>Home</span><span class="sep">|</span><span>Use Cases</span><span class="sep">|</span><span>Cloud Services</span><span class="sep">|</span><span>Pail's Infrastructure</span><span class="sep">|</span><span>Our Company</span><span class="sep">|</span><span>Contact Us</span>
  </div>
  <div class="abs copyright">© 2015 Nimbo-Pails.net. All Rights Reserved.</div>
</footer>

</body>
</html>
```